CuraNex System Web Page Design

This project is to design 6 pages of a web based medical system for clinics, hospitals, drugs suppliers, general items suppliers, insurance company, laboratories and patients (basically all parties which could be involved in).We want the designs of the browser, button, icon and layout are based on Vex, which is user friendly, looks professional, simple and neat but with powerful functions. We have uploaded few pictures of another system, please do not copy its design because this is not what we are looking for, the pictures are for you to know the elements should be included in our pages. CuraNex web-base system, design 6 pages1. Login PageShould include the following elements-company id with input field-login id with input field-password with input field2. Main Page (Navigation page)Should include the following elements-Appointment-Consultation-Patient-Drugs inventory -General supplies inventory -Laboratory-Suppliers-Insurance-Reports 3. Appointment PageShould include all the the elements in the respective pictures plus the followings-Daily View, Weekly View, Monthly View buttons4. Consultation PageShould include all the the elements in the respective picture5. Patient Page5.1 General information Should include all the the elements in the respective picture5.2 medical history/lab reportsShould include all the the elements in the respective picture plus the followings-Notify patient button-Share report button.
Updated on 28 Nov:
Please stop using Ward Keystone in your designs which is not the name of our system. We have just rename our system to CuraNex, please take note.
We need the system to look professional not playful, do not use too many colors and playful icons.
professional users

```html
<!DOCTYPE html>
<html lang="en">
<head>
<meta charset="utf-8">
<title>CuraNex System</title>
<link rel="stylesheet" href="https://fonts.googleapis.com/css2?family=Inter:wght@400;600&display=swap">
<style>
:root{
  --page-bg:#dedede;
  --window-bg:#f4f5f6;
  --titlebar-bg:#ececec;
  --titlebar-line:#d4d4d4;
  --text-main:#111111;
  --text-title:#3a3a3a;
  --tile-top:#cfe7fa;
  --tile-mid:#9fd1f4;
  --tile-bottom:#dff6fc;
  --tile-active:#2a72bd;
  --icon-line:#2868ad;
  --icon-active:#ffffff;
  --btn-close:#f25f57;
  --btn-min:#f8bd2e;
  --btn-max:#29c940;
}
*{box-sizing:border-box;margin:0;padding:0}
html,body{width:1200px;height:761px;overflow:hidden}
body{background:var(--page-bg);font-family:"Inter",Helvetica,Arial,sans-serif;position:relative}
.app-window{
  position:absolute;left:37px;top:60px;width:1128px;height:640px;
  background:linear-gradient(135deg,#ffffff 0%,#f3f4f5 40%,#e9eaec 70%,#f2f3f4 100%);
  border-radius:6px;overflow:hidden;
  box-shadow:0 18px 40px rgba(0,0,0,.35),0 0 0 1px rgba(0,0,0,.08);
}
.title-bar{
  height:29px;background:var(--titlebar-bg);border-bottom:1px solid var(--titlebar-line);
  position:relative;text-align:center;line-height:29px;font-size:16px;color:var(--text-title);
}
.traffic-lights{position:absolute;left:13px;top:8px;display:flex;gap:9px}
.traffic-lights span{width:13px;height:13px;border-radius:50%;display:block}
.light-close{background:var(--btn-close)}
.light-min{background:var(--btn-min)}
.light-max{background:var(--btn-max)}
.expand-icon{position:absolute;right:10px;top:7px}
.welcome{
  position:absolute;left:0;width:100%;top:93px;text-align:center;
  font-size:26px;font-weight:400;color:var(--text-main);
}
.module{position:absolute;width:177px;text-align:center}
.module-tile{
  width:177px;height:110px;display:flex;align-items:center;justify-content:center;
  background:linear-gradient(to bottom,var(--tile-top) 0%,var(--tile-mid) 62%,var(--tile-bottom) 100%);
}
.module-tile svg{width:74px;height:74px;fill:none;stroke:var(--icon-line);stroke-width:2.4;stroke-linecap:round;stroke-linejoin:round}
.module.is-active .module-tile{background:var(--tile-active)}
.module.is-active .module-tile svg{stroke:var(--icon-active)}
.module-label{margin-top:12px;font-size:19px;line-height:25px;color:var(--text-main)}
.module.is-active .module-label{font-weight:600}
.cursor{position:absolute;right:8px;bottom:8px}
</style>
</head>
<body>
<div class="app-window">
  <div class="title-bar">
    <div class="traffic-lights"><span class="light-close"></span><span class="light-min"></span><span class="light-max"></span></div>
    CuraNex System
    <svg class="expand-icon" width="15" height="15" viewBox="0 0 15 15" fill="none" stroke="#9a9a9a" stroke-width="1.6"><path d="M9 1h5v5M14 1L9 6M6 14H1V9M1 14l5-5"/></svg>
  </div>
  <h1 class="welcome">Welcome to CuraNex System</h1>

  <div class="module" style="left:43px;top:184px">
    <div class="module-tile"><svg viewBox="0 0 64 64"><circle cx="26" cy="18" r="10"/><path d="M8 52v-6c0-9 8-15 18-15h4"/><path d="M8 52h26"/><circle cx="44" cy="44" r="11"/><path d="M44 38v7h5"/></svg></div>
    <div class="module-label">Appointment</div>
  </div>
  <div class="module is-active" style="left:260px;top:184px">
    <div class="module-tile" style="position:relative"><svg viewBox="0 0 64 64"><rect x="22" y="8" width="20" height="12" rx="2"/><path d="M18 14h4M42 14h4"/><circle cx="10" cy="20" r="5"/><circle cx="54" cy="20" r="5"/><path d="M4 42V32c0-4 3-6 6-6h8v10M60 42V32c0-4-3-6-6-6h-8v10"/><path d="M14 30h36v6H14z"/><path d="M24 36v20M40 36v20M4 42h10v14M60 42H50v14"/><path d="M28 30v-4M36 30v-4"/></svg>
      <svg class="cursor" width="16" height="22" viewBox="0 0 16 22" style="width:16px;height:22px;stroke:#222;stroke-width:1;fill:#fff"><path d="M1 1v17l4-4 3 7 3-1-3-7h6z"/></svg></div>
    <div class="module-label">Consultation</div>
  </div>
  <div class="module" style="left:475px;top:184px">
    <div class="module-tile"><svg viewBox="0 0 64 64"><circle cx="32" cy="14" r="8"/><path d="M16 58V34c0-7 6-12 12-12h8c6 0 12 5 12 12v24"/><path d="M22 38l10 8 6-6"/><path d="M24 58V46M40 58V44"/></svg></div>
    <div class="module-label">Patient</div>
  </div>
  <div class="module" style="left:692px;top:184px">
    <div class="module-tile"><svg viewBox="0 0 64 64"><rect x="16" y="4" width="32" height="56" rx="3"/><path d="M16 14h32"/><path d="M22 9h20"/><rect x="22" y="20" width="20" height="10" rx="2"/><circle cx="26" cy="40" r="3"/><circle cx="38" cy="40" r="3"/><circle cx="26" cy="50" r="3"/><circle cx="38" cy="50" r="3"/></svg></div>
    <div class="module-label">Drugs Inventory</div>
  </div>
  <div class="module" style="left:907px;top:184px">
    <div class="module-tile"><svg viewBox="0 0 64 64"><rect x="8" y="12" width="38" height="42" rx="2"/><path d="M15 22h18M15 30h22M15 38h14M15 46h18"/><path d="M38 40l16-22 5 4-16 22-7 2z"/></svg></div>
    <div class="module-label">General Supplies<br>Inventory</div>
  </div>

  <div class="module" style="left:150px;top:398px">
    <div class="module-tile"><svg viewBox="0 0 64 64"><path d="M20 10h10M23 10v16L10 52c-1 3 1 6 4 6h22c3 0 5-3 4-6L27 26V10"/><path d="M14 44h22"/><path d="M46 8v44c0 4 6 4 6 0V8M44 8h10"/><path d="M46 30h6"/><circle cx="10" cy="14" r="2"/><circle cx="14" cy="22" r="2"/></svg></div>
    <div class="module-label">Laboratory</div>
  </div>
  <div class="module" style="left:367px;top:398px">
    <div class="module-tile"><svg viewBox="0 0 64 64"><circle cx="20" cy="12" r="6"/><path d="M12 40V26c0-4 3-6 6-6h4c4 0 6 2 6 6v14M16 40v18M24 40v18"/><path d="M38 20v34h16"/><circle cx="40" cy="56" r="3"/><circle cx="54" cy="56" r="3"/></svg></div>
    <div class="module-label">Suppliers</div>
  </div>
  <div class="module" style="left:582px;top:398px">
    <div class="module-tile"><svg viewBox="0 0 64 64"><path d="M6 32C6 18 18 8 32 8s26 10 26 24c-4-4-9-4-13 0-4-4-9-4-13 0-4-4-9-4-13 0-4-4-9-4-13 0z"/><path d="M32 8v44c0 4-3 6-6 6s-5-2-5-5"/><path d="M32 8c-6 6-7 16-6 24M32 8c6 6 7 16 6 24"/></svg></div>
    <div class="module-label">Insurance</div>
  </div>
  <div class="module" style="left:799px;top:398px">
    <div class="module-tile"><svg viewBox="0 0 64 64"><rect x="12" y="8" width="40" height="52" rx="3"/><rect x="24" y="4" width="16" height="8" rx="2"/><path d="M20 22h24M20 30h24M20 38h24M20 46h16"/></svg></div>
    <div class="module-label">Reports</div>
  </div>
</div>
</body>
</html>
```